Health & Safety Consultancy Business Card Design

DLT Secure Management specialises in OHS systems development (policies, procedures etc), providing advice and solutions with regard to all health and safety matters, conducts incident investigations and audits, as well as other OHS functions. The goal is to provide tailored solutions (i.e. not "off the shelf") to a wide range of businesses, primarily in the construction/mining/heavy industries, from large scale, national organisations to local small businesses who may not have a full time employee dedicated to health and safety in relation to their business activities.

Very sorry, I wish I had even the slightest idea with regard to a logo, but I'm open to all ideas!

Target Market(s)

Managers and other professionals of small to mid-tier companies within the construction/mining/heavy industries.

Industry/Entity Type

Health

Contact Information for Business Card

Tanvir Osei
Principal Consultant
DLT Safety Management
Tailored | Comprehensive | Practical
Phone: 0417 586 902
Email: enquiries@dltadvisory-example.net
PO Box 487, Fernvale Ridge 9021

Font styles to use
Sans Serif

Colors
3277b5
00a88f
f04a50

Requirements
Must have
• I'd like the back of the card to have a short list (5 or so items) of what the business offers, for example:

Practical advise and solutions
Development of OHS systems
Compliance auditing
Staff training and assessment
Incident investigation
Nice to have
• Would be great if we could steer clear of a bland white background - thumbs up to the darker colours.

My uSlate isn't liking the Look and Feel slider however the look and feel I'm aiming for is:

About midway between elegant and bold;
Slightly more on the serious side;
Definitely on the modern side;
Both personable yet professional;
More on the masculine side (although I am female!);
Midway between colourful and conservative; and finally,
A bit on the upmarket side wouldn't hurt, but not so much to give off a pompous impression.

```html
<!DOCTYPE html>
<html lang="en">
<head>
<meta charset="utf-8">
<title>DLT Safety Management – Business Card</title>
<link rel="stylesheet" href="https://fonts.googleapis.com/css2?family=Open+Sans:wght@400;600;700&family=Michroma&display=swap">
<style>
  :root {
    --stage: #e9e6e2;
    --card-white: #ffffff;
    --ink: #1e1e1e;
    --ink-soft: #444444;
    --brand-red: #d7191f;
    --band-black: #0d0d0d;
    --back-top: #2a2a2a;
    --back-bottom: #080808;
    --list-grey: #cfcfcf;
  }
  * { box-sizing: border-box; margin: 0; padding: 0; }
  html, body {
    width: 1200px; height: 784px; overflow: hidden;
    background: var(--stage);
    font-family: "Open Sans", Arial, sans-serif;
  }
  .card-sheet {
    position: relative; width: 1200px; height: 784px;
    display: flex; align-items: center; justify-content: center; gap: 40px;
  }
  .card {
    position: relative; width: 560px; height: 340px;
    border-radius: 6px; overflow: hidden;
    box-shadow: 0 4px 14px rgba(0,0,0,0.18);
  }

  /* Back side */
  .card-back {
    background: radial-gradient(ellipse at 50% 45%, var(--back-top) 0%, #151515 60%, var(--back-bottom) 100%);
    color: var(--list-grey);
    text-align: center;
  }
  .back-brand {
    display: flex; align-items: center; justify-content: center; gap: 12px;
    margin-top: 30px;
  }
  .brand-dot {
    display: inline-block; border-radius: 50%;
    background: var(--brand-red); flex: none;
  }
  .card-back .brand-dot { width: 40px; height: 40px; }
  .brand-name {
    font-family: "Open Sans", Arial, sans-serif;
    font-weight: 700; line-height: 1; text-align: left;
  }
  .brand-name .brand-initials { display: block; }
  .brand-name .brand-sub { display: block; letter-spacing: 2px; text-transform: uppercase; margin-top: 3px; }
  .card-back .brand-name { color: #e6e6e6; }
  .card-back .brand-initials { font-size: 30px; }
  .card-back .brand-sub { font-size: 8px; }
  .service-list {
    list-style: none; margin-top: 34px;
    font-family: "Michroma", "Open Sans", sans-serif;
    font-size: 14px; letter-spacing: 3px; line-height: 34px;
    font-variant: small-caps;
  }
  .service-list li:nth-child(4) { color: #b9b9b9; }
  .service-list li:nth-child(5) { color: #8e8e8e; }

  /* Front side */
  .card-front { background: var(--card-white); color: var(--ink); }
  .front-brand {
    position: absolute; left: 34px; top: 40px;
    display: flex; align-items: center; gap: 14px;
  }
  .card-front .brand-dot { width: 74px; height: 74px; }
  .card-front .brand-name { color: var(--ink); }
  .card-front .brand-initials { font-size: 52px; }
  .card-front .brand-sub { font-size: 11px; }
  .contact-person { position: absolute; left: 42px; top: 168px; }
  .person-name { color: var(--brand-red); font-weight: 700; font-size: 20px; line-height: 1.1; }
  .person-role { font-size: 12px; color: var(--ink); margin-top: 2px; }
  .contact-list {
    position: absolute; left: 42px; top: 222px;
    list-style: none; font-size: 14px; color: var(--ink-soft); line-height: 21px;
  }
  .contact-list li { display: flex; align-items: center; gap: 8px; white-space: nowrap; }
  .contact-icon { width: 13px; height: 13px; fill: var(--brand-red); flex: none; }
  .front-band {
    position: absolute; left: 0; right: 0; bottom: 0; height: 40px;
    background: var(--band-black);
    border-top: 3px solid var(--brand-red);
    display: flex; align-items: center; justify-content: center;
  }
  .tagline {
    font-family: "Michroma", "Open Sans", sans-serif;
    color: var(--brand-red); font-size: 11px; letter-spacing: 4px; text-transform: uppercase;
    white-space: nowrap;
  }
  .tagline .divider { color: #7a7a7a; margin: 0 10px; }
</style>
</head>
<body>
<main class="card-sheet">
  <section class="card card-back" aria-label="Card back">
    <div class="back-brand">
      <span class="brand-dot"></span>
      <span class="brand-name"><span class="brand-initials">DLT</span><span class="brand-sub">Safety Management</span></span>
    </div>
    <ul class="service-list">
      <li>Practical advise and solutions</li>
      <li>Development of OHS systems</li>
      <li>Compliance auditing</li>
      <li>Staff training and assessment</li>
      <li>Incident investigation</li>
    </ul>
  </section>

  <section class="card card-front" aria-label="Card front">
    <div class="front-brand">
      <span class="brand-dot"></span>
      <span class="brand-name"><span class="brand-initials">DLT</span><span class="brand-sub">Safety Management</span></span>
    </div>
    <div class="contact-person">
      <p class="person-name">Tanvir Osei</p>
      <p class="person-role">Principal Consultant</p>
    </div>
    <ul class="contact-list">
      <li>
        <svg class="contact-icon" viewBox="0 0 24 24" aria-hidden="true"><path d="M6.6 10.8a15.1 15.1 0 0 0 6.6 6.6l2.2-2.2a1 1 0 0 1 1-.25 11.4 11.4 0 0 0 3.6.57 1 1 0 0 1 1 1V20a1 1 0 0 1-1 1A17 17 0 0 1 3 4a1 1 0 0 1 1-1h3.5a1 1 0 0 1 1 1c0 1.25.2 2.45.57 3.6a1 1 0 0 1-.25 1z"/></svg>
        0417 586 902
      </li>
      <li>
        <svg class="contact-icon" viewBox="0 0 24 24" aria-hidden="true"><path d="M2 5h20v14H2z M4 7v.4l8 5.1 8-5.1V7z" fill-rule="evenodd"/></svg>
        enquiries@dltadvisory-example.net
      </li>
      <li>
        <svg class="contact-icon" viewBox="0 0 24 24" aria-hidden="true"><path d="M12 3 2 12h3v9h5v-6h4v6h5v-9h3z"/></svg>
        PO Box 487, Fernvale Ridge 9021
      </li>
    </ul>
    <div class="front-band">
      <p class="tagline">Tailored<span class="divider">|</span>Comprehensive<span class="divider">|</span>Practical</p>
    </div>
  </section>
</main>
</body>
</html>
```